Label for Dog Nourishing CBD Balm

Dear Designers,

We are looking for a packaging expert to design our new Hydrating Balm for dogs which contain a relaxing hemp extract (CBD). The product is intended to be massaged on the dog’s paws to make them softer and promote the animal’s well-being :)

Our company is already selling various relaxing cat & dog products, and we would like this new design to reflect the same "style & feeling" as our current products (see attached ZIP file).

Technical aspects:
- The packaging is a 40ml aluminium jar (58mm x 23mm).
- We are looking to design 2 separate labels (one for the front, one for the back)
- The label dimensions should be : 50mm x 50mm
- Please follow technical guidelines from printer (see ZIP file).

Design aspects:
- The design should be compatible with our brand identity (i.e. fluffly, pure, relaxing, positive, clean & natural).
- People should understand what the product "is" and what the product "does" simply from looking at the design.
- The actual balm is white/yellow in color.
- Soft/rounded shapes are preferred.
- Please use our brand's colors (see typo & colors in ZIP file)
- Please use our brand's fonts (see typo & colors in ZIP file)
- Please use our company logo (see ZIP file).
- The design also needs to convey a strong sense of professionalism as we are an animal "healthcare" brand.
- If you want to include a dog picture, we would prefer you to use a picture of our official brand ambassador (see ZIP file).
- Only original work (no plagiarism will be accepted).

Please don't hesitate to send us a message if you have any questions about the brand, the product or the design requirements.

We look forward to seeing your designs & working on this together !

Thanks & regards,
Marcus

Target Market(s)

Dog owners

Font styles to use
Other font styles liked:
• See ZIP file

Requirements
Must have
• Brand fonts (see typo & colors in ZIP file)
Brand colors (see typo & colors in ZIP file)

```html
<!DOCTYPE html>
<html lang="en">
<head>
<meta charset="utf-8">
<title>Verdalis Soothing Balm – Label Concepts</title>
<link rel="stylesheet" href="https://fonts.googleapis.com/css2?family=Cabin:wght@400;500;600&display=swap">
<style>
  :root {
    --teal: #3a9e7e;
    --teal-deep: #2a8a6b;
    --forest: #17311f;
    --orange: #e9a83c;
    --yellow: #e4dc38;
    --beige: #dcd9bd;
    --ink: #2a2a2a;
    --wave-line: #4a4a42;
    --photo-light: #e9e6e2;
    --photo-mid: #b3a6a0;
    --page: #ffffff;
  }
  * { box-sizing: border-box; margin: 0; padding: 0; }
  html, body { width: 1200px; height: 942px; overflow: hidden; background: var(--page); }
  body { position: relative; font-family: "Cabin", sans-serif; color: var(--ink); }

  .sheet-tag { position: absolute; font-size: 15px; letter-spacing: 1px; color: var(--ink); }

  .label {
    position: absolute; width: 425px; height: 423px; overflow: hidden;
    background: #fff; box-shadow: 3px 4px 6px rgba(0,0,0,.28);
  }
  .label svg.backdrop { position: absolute; inset: 0; }
  .label > * { position: absolute; }

  .brand { display: flex; align-items: center; gap: 8px; font-weight: 600; color: var(--forest); letter-spacing: 1px; }
  .brand-dot { width: 12px; height: 12px; border-radius: 50%; background: var(--teal); }

  .title { font-weight: 500; color: var(--forest); letter-spacing: 2.5px; white-space: nowrap; }
  .title .accent { color: var(--teal-deep); }

  .photo { background: radial-gradient(ellipse at 50% 40%, var(--photo-light), var(--photo-mid) 85%, rgba(179,166,160,0) 100%); border-radius: 40% 40% 10% 10%; }

  /* Pack 1 front */
  .benefits-row { font-size: 21px; letter-spacing: 1.5px; color: var(--forest); display: flex; gap: 14px; }
  .benefits-row span::before { content: ""; display: inline-block; width: 9px; height: 9px; border-radius: 50%; background: var(--teal); margin-right: 4px; vertical-align: 3px; }
  .dose-line { font-size: 18px; color: var(--forest); padding-bottom: 6px; border-bottom: 1.5px solid var(--teal); width: 140px; }
  .net-weight { font-size: 26px; color: var(--forest); }

  /* Pack 2 front */
  .pill { height: 27px; border-radius: 0 14px 14px 0; background: linear-gradient(90deg, var(--teal), var(--yellow)); font-size: 18px; color: var(--forest); padding-left: 14px; line-height: 27px; }
  .pill::before { content: ""; display: inline-block; width: 6px; height: 6px; border-radius: 50%; background: #fff; margin-right: 4px; vertical-align: 3px; }
  .benefits-bar { display: flex; font-size: 21px; letter-spacing: 2px; color: var(--forest); }
  .benefits-bar span { padding: 0 10px; border-left: 1.5px solid rgba(255,255,255,.6); }
  .benefits-bar span:first-child { border-left: 0; }

  /* Backs */
  .copy { font-size: 12.5px; line-height: 1.17; color: var(--forest); }
  .copy h3 { font-size: 12.5px; font-weight: 500; letter-spacing: .5px; }
  .copy p + h3 { margin-top: 14px; }
  .distributor { font-size: 12.5px; line-height: 1.2; color: var(--forest); }
  .col-head { display: flex; align-items: center; gap: 8px; font-size: 12.5px; font-weight: 500; letter-spacing: .5px; color: var(--forest); }
  .col-head::before { content: ""; width: 10px; height: 12px; border-radius: 0 6px 6px 0; background: linear-gradient(90deg, var(--teal), var(--yellow)); }
  .col-text { font-size: 12.5px; line-height: 1.2; color: var(--forest); }
</style>
</head>
<body>

<div class="sheet-tag" style="left:18px; top:124px;">PACK 1</div>
<div class="sheet-tag" style="left:18px; top:257px;">FRONT</div>
<div class="sheet-tag" style="left:18px; top:689px;">BACK</div>
<div class="sheet-tag" style="left:1097px; top:124px;">PACK 2</div>
<div class="sheet-tag" style="left:1097px; top:257px;">FRONT</div>
<div class="sheet-tag" style="left:1097px; top:689px;">BACK</div>

<!-- Pack 1 front -->
<section class="label" style="left:112px; top:32px;">
  <svg class="backdrop" width="425" height="423" viewBox="0 0 425 423">
    <rect width="425" height="423" fill="var(--orange)"/>
    <circle cx="192" cy="216" r="243" fill="var(--teal)"/>
    <circle cx="180" cy="222" r="222" fill="#fff"/>
  </svg>
  <div class="brand" style="left:120px; top:100px; font-size:34px;"><i class="brand-dot"></i>VERDALIS</div>
  <div class="title" style="left:42px; top:162px; font-size:37px;">SOOTHING <span class="accent">BALM</span></div>
  <div class="benefits-row" style="left:44px; top:212px;"><span>REPAIR</span><span>NOURISH</span><span>PROTECT</span></div>
  <div class="photo" role="img" aria-label="Photo of the brand ambassador dog in a knitted sweater" style="left:0; top:258px; width:185px; height:165px;"></div>
  <div class="dose-line" style="left:278px; top:270px;">CBD 250mg</div>
  <div class="dose-line" style="left:278px; top:300px;">0% THC</div>
  <div class="net-weight" style="left:372px; top:378px;">40g</div>
</section>

<!-- Pack 2 front -->
<section class="label" style="left:652px; top:32px;">
  <svg class="backdrop" width="425" height="423" viewBox="0 0 425 423">
    <defs>
      <linearGradient id="topBand" x1="0" y1="0" x2="1" y2="0.3">
        <stop offset="0" stop-color="var(--teal)"/><stop offset="1" stop-color="var(--yellow)"/>
      </linearGradient>
      <linearGradient id="bottomBand" x1="0" y1="0" x2="0" y2="1">
        <stop offset="0" stop-color="var(--yellow)"/><stop offset=".6" stop-color="var(--teal)"/>
      </linearGradient>
    </defs>
    <path d="M0 0H425V42C330 20 250 30 170 50C100 66 45 55 0 35Z" fill="url(#topBand)"/>
    <path d="M0 20C45 45 100 56 170 42C250 24 330 14 425 38" fill="none" stroke="var(--wave-line)" stroke-width="3"/>
    <path d="M0 345C110 370 220 390 330 370C370 362 400 352 425 342V423H0Z" fill="url(#bottomBand)"/>
    <path d="M150 382C230 392 300 382 425 342" fill="none" stroke="var(--wave-line)" stroke-width="3"/>
  </svg>
  <div class="brand" style="left:42px; top:84px; font-size:32px;"><i class="brand-dot"></i>VERDALIS</div>
  <div class="title" style="left:40px; top:138px; font-size:37px;">SOOTHING <span class="accent">BALM</span></div>
  <div class="pill" style="left:0; top:208px; width:125px;">CBD 250mg</div>
  <div class="pill" style="left:0; top:246px; width:106px;">0% THC</div>
  <div class="pill" style="left:0; top:282px; width:86px;">40g</div>
  <div class="photo" role="img" aria-label="Photo of the brand ambassador dog in a knitted sweater" style="left:192px; top:178px; width:178px; height:196px;"></div>
  <div class="benefits-bar" style="left:47px; top:386px;"><span>REPAIR</span><span>NOURISH</span><span>PROTECT</span></div>
</section>

<!-- Pack 1 back -->
<section class="label" style="left:112px; top:473px;">
  <svg class="backdrop" width="425" height="423" viewBox="0 0 425 423">
    <rect width="425" height="423" fill="var(--beige)"/>
    <circle cx="300" cy="280" r="285" fill="#cfe0d8" opacity=".8"/>
    <circle cx="310" cy="285" r="270" fill="#fff"/>
  </svg>
  <div class="copy" style="left:57px; top:58px; width:300px;">
    <h3>EVERYDAY RELAXATION</h3>
    <p>This balm repairs, nourishes and protects your dog's sensitive skin. Its trusted multi-action formula brings relief to fragile areas and soothes temporary irritations (paw pads, elbows, etc.)</p>
    <h3>RECOMMENDED USE:</h3>
    <p>Rub a small amount of balm in the palm of your hand and apply to sensitive areas as a daily care ritual. Repeat until the product has been completely absorbed.</p>
    <h3>INGREDIENTS:</h3>
    <p>Shea Butter, Beeswax, Coconut Oil, Hemp Extract (0% THC).</p>
  </div>
  <div class="brand" style="left:57px; top:300px; font-size:18px;"><i class="brand-dot" style="width:8px;height:8px;"></i>VERDALIS</div>
  <div class="distributor" style="left:57px; top:336px;">Distributed by:<br>VERDA EUROPE KFT.<br>Liget utca 14<br>1071 Budapest<br>Hungary</div>
  <div class="photo" role="img" aria-label="Photo of the brand ambassador dog holding a toy" style="left:272px; top:270px; width:153px; height:153px;"></div>
</section>

<!-- Pack 2 back -->
<section class="label" style="left:652px; top:473px;">
  <svg class="backdrop" width="425" height="423" viewBox="0 0 425 423">
    <defs>
      <linearGradient id="backBand" x1="0" y1="0" x2="0" y2="1">
        <stop offset="0" stop-color="var(--yellow)"/><stop offset=".7" stop-color="var(--teal)"/>
      </linearGradient>
    </defs>
    <path d="M0 358C120 372 240 392 330 380C370 374 400 364 425 352V423H0Z" fill="url(#backBand)"/>
    <path d="M180 388C260 392 330 382 425 350" fill="none" stroke="var(--wave-line)" stroke-width="3"/>
  </svg>
  <div class="col-head" style="left:0; top:22px;">EVERYDAY RELAXATION</div>
  <div class="col-text" style="left:17px; top:51px; width:185px;">This balm repairs, nourishes and protects your dog's sensitive skin. Its trusted multi-action formula brings relief to fragile areas and soothes temporary irritations (paw pads, elbows, etc.)</div>
  <div class="col-head" style="left:0; top:179px;">RECOMMENDED USE:</div>
  <div class="col-text" style="left:17px; top:208px; width:185px;">Rub a small amount of balm in the palm of your hand and apply to sensitive areas as a daily care ritual. Repeat until the product has been completely absorbed.</div>
  <div class="col-head" style="left:212px; top:22px;">INGREDIENTS:</div>
  <div class="col-text" style="left:229px; top:51px; width:185px;">Shea Butter, Beeswax, Coconut Oil, Hemp Extract (0% THC).</div>
  <div class="brand" style="left:272px; top:146px; font-size:18px;"><i class="brand-dot" style="width:8px;height:8px;"></i>VERDALIS</div>
  <div class="col-text" style="left:230px; top:181px; width:150px; text-align:center;">Distributed by:</div>
  <div class="col-text" style="left:230px; top:208px; width:150px; text-align:center; font-weight:500;">VERDA EUROPE KFT.<br>Liget utca 14<br>1071 Budapest<br>Hungary</div>
  <div class="photo" role="img" aria-label="Photo of the brand ambassador dog" style="left:250px; top:278px; width:112px; height:112px;"></div>
</section>

</body>
</html>
```